Cleaning Company Website Design

I am looking for a website design that has my contact information on each page (Call or Text and my e-mail). It should have the main landing page and than pages for Residential Cleaning (Move In/Move Out, Weekly, and Bi-Weekly Cleaning), Commercial Cleaning (Move In/Move Out, Weekly, and Bi-Weekly Cleaning), New Construction Cleaning (Residential, Commercial, and Industrial), and Apartment Turn cleaning for Property Managers. It should list that we carry insurance as well.

Target Market(s)

Residential and Commercial Customers

Industry/Entity Type

Cleaning

Coding

Coded - Design and coding required

Number of Pages Required

5+ page

Requirements
Must have
• A clean professional looking website

```html
<!DOCTYPE html>
<html lang="en">
<head>
<meta charset="utf-8">
<title>Brightway Cleaning</title>
<link href="https://fonts.googleapis.com/css2?family=Montserrat:wght@400;500;600;700;800&display=swap" rel="stylesheet">
<style>
:root{
  --navy:#15304c;
  --navy-deep:#102740;
  --teal:#2bb3a5;
  --teal-dark:#13897f;
  --blue:#2a86cf;
  --ink:#1d1d1d;
  --muted:#5d6670;
  --line:#d9dde2;
  --white:#ffffff;
}
*{box-sizing:border-box;margin:0;padding:0}
html,body{width:1200px;height:3817px;overflow:hidden}
body{font-family:'Montserrat',sans-serif;color:var(--ink);background:var(--white);position:relative}
.abs{position:absolute}
.btn{position:absolute;display:flex;align-items:center;justify-content:center;color:#fff;font-weight:700;font-size:12px;letter-spacing:.5px;text-transform:uppercase;border-radius:2px;white-space:nowrap}
.btn-blue{background:var(--blue)}
.btn-teal{background:var(--teal)}
.sec-title{position:absolute;left:0;width:1200px;text-align:center;font-weight:700;font-size:31px;letter-spacing:1px;text-transform:uppercase;color:var(--teal);white-space:nowrap}
.sec-title .dash{display:inline-block;width:20px;height:2px;background:var(--teal);vertical-align:middle;margin:0 10px}
.sec-title .alt{color:var(--blue)}

/* header */
.header{position:absolute;left:0;top:0;width:1200px;height:108px;background:#fff;z-index:2}
.contact-item{position:absolute;top:33px;display:flex;align-items:center;gap:8px;white-space:nowrap}
.contact-icon{width:26px;height:26px;border-radius:50%;border:1px solid var(--line);display:flex;align-items:center;justify-content:center;flex:none}
.contact-item small{display:block;font-size:7px;color:var(--teal);font-weight:600;letter-spacing:.4px}
.contact-item span{font-size:12px;color:var(--ink);font-weight:500}
.brand{position:absolute;left:520px;top:30px;width:160px;text-align:center;font-weight:700;font-size:17px;line-height:20px;color:var(--teal);letter-spacing:1px}
.socials{position:absolute;display:flex;gap:9px}
.socials i{display:block;width:24px;height:24px;border-radius:50%;border:1px solid #b8bec5}
.socials i.on{background:var(--teal);border-color:var(--teal)}
.nav{position:absolute;left:150px;top:93px;width:900px;height:31px;background:var(--blue);display:flex;align-items:center;padding-left:8px;z-index:3}
.nav a{color:#fff;font-size:11.5px;font-weight:500;padding:0 10px;height:23px;line-height:23px;text-decoration:none;white-space:nowrap}
.nav a.active{background:var(--teal)}

/* hero */
.hero{position:absolute;left:0;top:108px;width:1200px;height:490px;background:linear-gradient(90deg,#1a3552 0%,#1c3a58 55%,#173450 100%)}
.hero h1{position:absolute;left:181px;top:162px;color:#fff;font-weight:800;font-size:25px;line-height:31px;letter-spacing:.8px;text-transform:uppercase;white-space:nowrap}
.hero-photo{position:absolute;left:615px;top:0;width:422px;height:490px;background:radial-gradient(ellipse at 50% 55%,#2aa9a0 0%,#1f6f7c 40%,#1c3a58 75%)}

/* about */
.about-photos{position:absolute;left:150px;top:674px;width:444px;height:307px}
.about-photos div{position:absolute;top:0;height:100%}
.about-title{position:absolute;left:673px;top:703px;font-size:29px;font-weight:700;color:var(--teal);letter-spacing:1px}
.about-title .dash{display:inline-block;width:17px;height:2px;background:var(--teal);vertical-align:middle;margin-left:8px}
.about-lead{position:absolute;left:673px;top:756px;width:330px;font-size:14px;font-weight:600;line-height:19px}
.about-copy{position:absolute;left:673px;width:365px;font-size:12px;line-height:17.5px;color:var(--muted)}

/* services */
.services{position:absolute;left:0;top:1055px;width:1200px;height:533px;background:var(--navy)}
.services .sub{position:absolute;left:0;top:102px;width:1200px;text-align:center;color:#fff;font-size:13px}
.svc-card{position:absolute;top:145px;width:206px;height:252px;background:#fff;border:3px solid #fff}
.svc-card .ph{height:186px;width:100%}
.svc-card h3{text-align:center;font-size:14px;font-weight:700;margin-top:16px}
.svc-card p{text-align:center;font-size:12px;color:var(--muted);margin-top:2px}
.svc-card.hl h3,.svc-card.hl p{color:var(--teal)}
.svc-go{position:absolute;left:80px;top:155px;width:40px;height:40px;border-radius:50%;background:var(--teal);border:3px solid #fff;display:flex;align-items:center;justify-content:center}

/* process */
.step{position:absolute;top:1722px;width:230px;height:230px;border-radius:50%}
.step-inner{position:absolute;left:14px;top:14px;width:202px;height:202px;border-radius:50%;background:#f4f5f6;box-shadow:0 10px 20px rgba(0,0,0,.12);display:flex;flex-direction:column;align-items:center;padding-top:32px}
.step-inner h4{font-size:15px;font-weight:700;margin-top:12px;letter-spacing:.5px}
.step-inner p{font-size:11px;color:var(--muted);text-align:center;width:140px;line-height:14.5px;margin-top:5px}

/* packages */
.packages{position:absolute;left:0;top:2024px;width:1200px;height:577px;background:var(--navy)}
.plan{position:absolute;background:#fff;text-align:center}
.plan h4{font-size:16px;font-weight:700;letter-spacing:.5px}
.plan .price{font-size:30px;font-weight:700;color:var(--blue);margin-top:12px}
.plan .price sup{font-size:12px;font-weight:400;color:var(--muted);vertical-align:top;position:relative;top:6px}
.plan .desc{font-size:11px;line-height:15px;color:var(--muted);width:172px;margin:14px auto 0}
.plan ul{list-style:none;text-align:left;margin:20px 0 0 26px}
.plan li{font-size:11px;color:var(--muted);display:flex;align-items:center;gap:9px;height:22.5px}
.plan li i{width:11px;height:11px;border-radius:50%;background:#e8ebee;display:inline-block;position:relative}
.plan li i::after{content:"";position:absolute;left:3px;top:4px;width:5px;height:3px;border-top:1.5px solid #7d868f}
.plan.featured{background:linear-gradient(180deg,#17a79a 0%,#10857c 100%);border:2px solid #19b3a4;box-shadow:0 0 0 2px #0f6c66}
.plan.featured h4,.plan.featured .price,.plan.featured .desc,.plan.featured li{color:#fff}
.plan.featured .price sup{color:#e0f5f2}
.plan.featured li i{background:var(--blue)}
.plan.featured li i::after{border-color:#fff}

/* testimonial */
.quote-mark{position:absolute;left:576px;top:2734px;width:48px;height:48px;border-radius:50%;background:var(--blue);display:flex;align-items:center;justify-content:center;color:#fff;font-size:34px;font-weight:800;line-height:1}
.testi-text{position:absolute;left:285px;top:2803px;width:630px;text-align:center;font-size:12.5px;line-height:19px;color:#333}
.author{position:absolute;left:528px;top:2897px;display:flex;align-items:center;gap:10px}
.author .av{width:38px;height:38px;border-radius:50%;background:linear-gradient(135deg,#c9a38a,#8b6b58);border:2px solid #eee}
.author b{display:block;font-size:12px;color:var(--blue);font-weight:600}
.author small{font-size:11px;color:var(--muted)}
.dots{position:absolute;left:569px;top:2963px;display:flex;gap:8px}
.dots i{width:9px;height:9px;border-radius:50%;border:1px solid #8b939b}
.dots i.on{border-color:var(--teal);background:#fff;box-shadow:inset 0 0 0 2px #fff,inset 0 0 0 5px var(--teal)}

/* quote */
.quote-card{position:absolute;left:156px;top:3052px;width:893px;height:355px;background:#fff;box-shadow:0 0 22px rgba(0,0,0,.08)}
.quote-photo{position:absolute;left:0;top:0;width:419px;height:355px;background:linear-gradient(135deg,#c7d3dc 0%,#9fb6c4 45%,#d7b84a 80%,#e5c94c 100%)}
.overlay{position:absolute;left:112px;top:71px;width:196px;height:219px;background:rgba(17,38,58,.92);text-align:center;padding-top:30px}
.overlay h3{color:var(--teal);font-size:20px;font-weight:600;line-height:23px;letter-spacing:1px}
.overlay p{color:#fff;font-size:12px;line-height:17px;margin-top:12px;padding:0 14px}
.field{position:absolute;border:1px solid var(--line);font-size:11px;color:#8b939b;padding:10px 12px;background:#fff}

/* footer */
.footer{position:absolute;left:0;top:3486px;width:1200px;height:287px;background:var(--navy)}
.footer h5{position:absolute;top:68px;font-size:14px;font-weight:700;color:var(--teal);letter-spacing:.8px}
.footer .row{position:absolute;display:flex;gap:10px;color:#fff;font-size:12px;line-height:18px;white-space:nowrap}
.footer .links{position:absolute;left:594px;top:100px;font-size:12px;color:#fff;line-height:18.8px}
.footer .links .cur{color:var(--teal);text-decoration:underline}
.copy-bar{position:absolute;left:0;top:3773px;width:1200px;height:44px;background:var(--blue)}
.copy-bar p{position:absolute;left:150px;top:14px;color:#fff;font-size:11.5px}
</style>
</head>
<body>

<header class="header">
  <div class="contact-item" style="left:149px">
    <div class="contact-icon"><svg width="12" height="12" viewBox="0 0 24 24"><path d="M6.6 10.8a15 15 0 0 0 6.6 6.6l2.2-2.2a1 1 0 0 1 1-.25 11.4 11.4 0 0 0 3.6.6 1 1 0 0 1 1 1V20a1 1 0 0 1-1 1A17 17 0 0 1 3 4a1 1 0 0 1 1-1h3.5a1 1 0 0 1 1 1c0 1.25.2 2.45.6 3.6a1 1 0 0 1-.25 1z" fill="#2a86cf"/></svg></div>
    <div><small>CALL NOW</small><span>(555) 014-2290</span></div>
  </div>
  <div class="contact-item" style="left:277px">
    <div class="contact-icon"><svg width="12" height="10" viewBox="0 0 24 18"><rect x="1" y="1" width="22" height="16" rx="2" fill="#2a86cf"/><path d="M2 2l10 8 10-8" stroke="#fff" stroke-width="2" fill="none"/></svg></div>
    <div><small>EMAIL</small><span>hello@brightway.example</span></div>
  </div>
  <div class="brand">BRIGHTWAY<br>CLEANING</div>
  <div class="socials" style="left:776px;top:31px"><i></i><i class="on"></i><i></i><i></i></div>
  <div class="btn btn-teal" style="left:925px;top:28px;width:125px;height:30px">Get a Quote</div>
</header>
<nav class="nav">
  <a class="active">Home</a><a>About</a><a>Residential Cleaning</a><a>Commercial Cleaning</a><a>Construction Cleaning</a><a>Apartment Turn cleaning</a><a>Packages</a><a>Contact Us</a>
</nav>

<section class="hero">
  <h1>Quality driven &amp;<br>reliable to take care<br>of all your cleaning<br>needs!!!</h1>
  <div class="btn btn-blue" style="left:181px;top:304px;width:133px;height:29px">Appointment</div>
  <div class="hero-photo" role="img" aria-label="Smiling cleaner in yellow gloves holding a bucket of cleaning supplies"></div>
</section>

<section>
  <div class="about-photos">
    <div role="img" aria-label="Cleaner in navy overalls" style="left:0;width:150px;background:linear-gradient(180deg,#e9ecef,#27344a)"></div>
    <div role="img" aria-label="Cleaner in green apron" style="left:155px;width:140px;background:linear-gradient(180deg,#eef0f2,#2faa5b)"></div>
    <div role="img" aria-label="Cleaner holding spray bottle" style="left:300px;width:144px;background:linear-gradient(180deg,#eceef0,#5b4636)"></div>
  </div>
  <div class="about-title">ABOUT US<span class="dash"></span></div>
  <div class="about-lead">Lorem Ipsum is simply dummy text of the printing and typesetting industry.</div>
  <p class="about-copy" style="top:810px">Lorem Ipsum has been the industry's standard dummy text ever since the 1500s, when an unknown printer took a galley of type and scrambled it to make a type specimen book.</p>
  <p class="about-copy" style="top:880px">It has survived not only five centuries, but also the leap into electronic typesetting, remaining essentially unchanged.</p>
  <div class="btn btn-teal" style="left:673px;top:942px;width:117px;height:29px">Read More</div>
</section>

<section class="services">
  <div class="sec-title" style="top:66px"><span class="dash"></span>Cleaning <span class="alt">Services</span><span class="dash"></span></div>
  <div class="sub">We carry insurance as well</div>
  <div class="svc-card" style="left:150px"><div class="ph" role="img" aria-label="Cleaners wiping a living room floor" style="background:linear-gradient(135deg,#d9dde3,#8a8fa8)"></div><h3>Residential</h3><p>Cleaning</p></div>
  <div class="svc-card" style="left:381px"><div class="ph" role="img" aria-label="Cleaners working in an office" style="background:linear-gradient(135deg,#d0d6dc,#55708e)"></div><h3>Commercial</h3><p>Cleaning</p></div>
  <div class="svc-card" style="left:612px"><div class="ph" role="img" aria-label="Worker in protective suit disinfecting" style="background:linear-gradient(135deg,#f2f4f6,#b4bdc6)"></div><h3>Antiviral</h3><p>Disinfection</p></div>
  <div class="svc-card hl" style="left:843px"><div class="ph" role="img" aria-label="Worker cleaning a construction site" style="background:linear-gradient(135deg,#3f7f8c,#1f5b6b)"></div><div class="svc-go"><svg width="14" height="14" viewBox="0 0 24 24"><path d="M4 12h14M13 6l6 6-6 6" stroke="#fff" stroke-width="2.5" fill="none"/></svg></div><h3>Construction</h3><p>Cleaning</p></div>
  <div class="btn btn-blue" style="left:481px;top:428px;width:238px;height:30px">Book Appointment on Call</div>
</section>

<section>
  <div class="sec-title" style="top:1653px"><span class="dash"></span>Working <span class="alt">Process</span><span class="dash"></span></div>
  <div class="step" style="left:255px;border:3px solid var(--teal)">
    <div class="step-inner">
      <svg width="48" height="50" viewBox="0 0 48 50" fill="none" stroke="#2a86cf" stroke-width="2"><rect x="3" y="7" width="42" height="40" rx="3"/><line x1="3" y1="17" x2="45" y2="17"/><line x1="13" y1="2" x2="13" y2="11"/><line x1="35" y1="2" x2="35" y2="11"/><g stroke-width="1.6"><rect x="9" y="23" width="6" height="5"/><rect x="18" y="23" width="6" height="5"/><rect x="27" y="23" width="6" height="5"/><rect x="36" y="23" width="5" height="5"/><rect x="9" y="33" width="6" height="5"/><rect x="18" y="33" width="6" height="5"/><rect x="27" y="33" width="6" height="5"/></g></svg>
      <h4>BOOK</h4><p>Lorem Ipsum is simply dummy text of the printing industry.</p>
    </div>
  </div>
  <div class="step" style="left:492px;border:3px solid var(--blue)">
    <div class="step-inner">
      <svg width="50" height="50" viewBox="0 0 50 50" fill="none" stroke="#2a86cf" stroke-width="2"><path d="M30 14l3 9 9 3-9 3-3 9-3-9-9-3 9-3z"/><path d="M14 20l2 5 5 2-5 2-2 5-2-5-5-2 5-2z"/><path d="M26 2l1.5 4 4 1.5-4 1.5L26 13l-1.5-4-4-1.5 4-1.5z"/></svg>
      <h4>CLEAN</h4><p>Lorem Ipsum is simply dummy text of the printing industry.</p>
    </div>
  </div>
  <div class="step" style="left:725px;border:3px solid var(--teal)">
    <div class="step-inner">
      <svg width="56" height="50" viewBox="0 0 56 50" fill="none" stroke="#2a86cf" stroke-width="2"><circle cx="40" cy="14" r="6"/><g stroke="#f2b01e"><line x1="40" y1="2" x2="40" y2="5"/><line x1="52" y1="14" x2="49" y2="14"/><line x1="31" y1="14" x2="28" y2="14"/><line x1="48" y1="6" x2="46" y2="8"/></g><path d="M4 36h36l8-10"/><line x1="10" y1="36" x2="6" y2="46"/><line x1="36" y1="36" x2="40" y2="46"/></svg>
      <h4>RELAX</h4><p>Lorem Ipsum is simply dummy text of the printing industry.</p>
    </div>
  </div>
  <svg class="abs" style="left:447px;top:1818px" width="72" height="38" viewBox="0 0 72 38"><path d="M4 19h52M44 6l14 13-14 13" stroke="#2bb3a5" stroke-width="6" fill="none"/><circle cx="6" cy="12" r="3" fill="#2a86cf"/><circle cx="6" cy="26" r="3" fill="#2a86cf"/></svg>
  <svg class="abs" style="left:682px;top:1818px" width="72" height="38" viewBox="0 0 72 38"><path d="M4 19h52M44 6l14 13-14 13" stroke="#2bb3a5" stroke-width="6" fill="none"/><circle cx="6" cy="12" r="3" fill="#2a86cf"/><circle cx="6" cy="26" r="3" fill="#2a86cf"/></svg>
</section>

<section class="packages">
  <div class="sec-title" style="top:68px"><span class="dash"></span>Our <span class="alt">Packages</span><span class="dash"></span></div>
  <div class="plan" style="left:246px;top:149px;width:219px;height:332px;padding-top:22px">
    <h4>BASIC PLAN</h4><div class="price">$128<sup>/mo</sup></div>
    <p class="desc">Lorem Ipsum is simply dummy text of the printing industry.</p>
    <ul><li><i></i>Floor Cleaning</li><li><i></i>General Dusting</li><li><i></i>Door Cleaned</li><li><i></i>Carpet Cleaning</li><li><i></i>Upholstery Cleaning</li></ul>
    <div class="btn btn-blue" style="left:27px;top:284px;width:88px;height:24px;font-weight:500;font-size:10.5px">Book Now</div>
  </div>
  <div class="plan featured" style="left:490px;top:129px;width:224px;height:373px;padding-top:19px">
    <h4>STANDARD PLAN</h4><div class="price" style="font-size:35px">$168<sup>/mo</sup></div>
    <p class="desc">Lorem Ipsum is simply dummy text of the printing industry.</p>
    <ul><li><i></i>Dusting &amp; Vacumming</li><li><i></i>Bathroom Cleaning</li><li><i></i>Emptying Trash</li><li><i></i>Carpet Cleaning</li><li><i></i>Roof Light Cleaning</li></ul>
    <div class="btn btn-teal" style="left:61px;top:304px;width:100px;height:29px;font-weight:500;font-size:10.5px;background:#2bc0b0">Book Now</div>
  </div>
  <div class="plan" style="left:741px;top:149px;width:219px;height:332px;padding-top:22px">
    <h4>GOLD PLAN</h4><div class="price">$199<sup>/mo</sup></div>
    <p class="desc">Lorem Ipsum is simply dummy text of the printing industry.</p>
    <ul><li><i></i>Bathroom Cleaning</li><li><i></i>Living Areas</li><li><i></i>Exterior Building</li><li><i></i>Full House</li><li><i></i>Wooden Polish</li></ul>
    <div class="btn btn-blue" style="left:65px;top:284px;width:88px;height:24px;font-weight:500;font-size:10.5px">Book Now</div>
  </div>
</section>

<section>
  <div class="sec-title" style="top:2667px"><span class="dash"></span>Client <span class="alt">Testimonials</span><span class="dash"></span></div>
  <div class="quote-mark">&ldquo;</div>
  <p class="testi-text">Lorem Ipsum is simply dummy text of the printing and typesetting industry. Lorem Ipsum has been the industry's standard dummy text ever since the 1500s, when an unknown printer took a galley of type and scrambled it to make a type specimen book. It has survived not only five centuries, but also the leap into electronic typesetting, remaining essentially unchanged.</p>
  <div class="author"><div class="av" role="img" aria-label="Client portrait"></div><div><b>Marek Lindqvist</b><small>Lorem Ipsum</small></div></div>
  <div class="dots"><i></i><i></i><i class="on"></i><i></i></div>
</section>

<section class="quote-card">
  <div class="quote-photo" role="img" aria-label="Mop cleaning a floor beside a bucket of supplies">
    <div class="overlay">
      <h3>AVAILABLE<br>PACKAGES</h3>
      <p>for Move In/Move Out, Weekly, and Bi-Weekly Cleaning</p>
      <div class="btn btn-blue" style="left:28px;top:165px;width:141px;height:28px;font-weight:600">Explore More</div>
    </div>
  </div>
  <div class="sec-title" style="left:454px;width:409px;top:36px;font-size:29px"><span class="dash"></span>Get a <span class="alt">Quote</span><span class="dash"></span></div>
  <div class="field" style="left:454px;top:89px;width:200px;height:32px">Name</div>
  <div class="field" style="left:663px;top:89px;width:200px;height:32px">Email</div>
  <div class="field" style="left:454px;top:135px;width:200px;height:32px">Phone</div>
  <div class="field" style="left:663px;top:135px;width:200px;height:32px">Services<span style="position:absolute;right:10px;top:8px;font-size:8px">&#9660;</span></div>
  <div class="field" style="left:454px;top:181px;width:409px;height:89px">Message</div>
  <div class="btn btn-blue" style="left:454px;top:283px;width:409px;height:28px;font-size:11px">Submit</div>
</section>

<footer class="footer">
  <div class="abs" style="left:150px;top:145px;font-weight:700;font-size:22px;color:var(--teal);letter-spacing:1px;line-height:28px">BRIGHTWAY<br>CLEANING</div>
  <h5 style="left:366px">CONATCT INFO</h5>
  <div class="row" style="left:366px;top:101px;width:200px"><svg width="12" height="16" viewBox="0 0 12 16"><path d="M6 0a6 6 0 0 1 6 6c0 4-6 10-6 10S0 10 0 6a6 6 0 0 1 6-6z" fill="#2bb3a5"/><circle cx="6" cy="6" r="2" fill="#15304c"/></svg><span>412 Lorem ipsum Maple Ave,<br>Fairview, CA 90000</span></div>
  <div class="row" style="left:366px;top:146px"><svg width="12" height="12" viewBox="0 0 24 24"><path d="M6.6 10.8a15 15 0 0 0 6.6 6.6l2.2-2.2a1 1 0 0 1 1-.25 11.4 11.4 0 0 0 3.6.6 1 1 0 0 1 1 1V20a1 1 0 0 1-1 1A17 17 0 0 1 3 4a1 1 0 0 1 1-1h3.5a1 1 0 0 1 1 1c0 1.25.2 2.45.6 3.6a1 1 0 0 1-.25 1z" fill="#2bb3a5"/></svg><span>(555) 017-4418</span></div>
  <div class="row" style="left:366px;top:176px"><svg width="13" height="10" viewBox="0 0 24 18"><rect x="1" y="1" width="22" height="16" rx="2" fill="#2bb3a5"/><path d="M2 2l10 8 10-8" stroke="#15304c" stroke-width="2" fill="none"/></svg><span>info@brightway.example</span></div>
  <div class="row" style="left:366px;top:208px"><svg width="13" height="13" viewBox="0 0 24 24"><circle cx="12" cy="12" r="10" fill="none" stroke="#2bb3a5" stroke-width="2.5"/><path d="M2 12h20M12 2c4 4 4 16 0 20M12 2c-4 4-4 16 0 20" stroke="#2bb3a5" stroke-width="2" fill="none"/></svg><span>live location</span></div>
  <h5 style="left:594px">QUICK LINK</h5>
  <div class="links"><div class="cur">Home</div><div>About</div><div>Residential Cleaning</div><div>Commercial Cleaning</div><div>Construction Cleaning</div><div>Apartment Turn cleaning</div><div>Packages</div><div>Contact Us</div></div>
  <h5 style="left:793px">STAY IN TOUCH</h5>
  <p class="abs" style="left:793px;top:96px;width:180px;color:#fff;font-size:12px;line-height:17px">Subscribe to our newsletter and stay updated</p>
  <div class="field" style="left:793px;top:139px;width:256px;height:29px;padding:7px 12px">Your email address*</div>
  <div class="btn btn-blue" style="left:793px;top:181px;width:150px;height:29px;font-size:11px">Subscribe Now</div>
</footer>
<div class="copy-bar">
  <p>&copy; 2024 Brightway Cleaning. All Right Reserved</p>
  <div class="socials" style="left:926px;top:10px;gap:8px"><i style="border-color:#fff"></i><i class="on" style="border-color:#fff"></i><i style="border-color:#fff"></i><i style="border-color:#fff"></i></div>
</div>

</body>
</html>
```